Online Psychology Practice needs business cards.

Online Psychology service needs business cards. Have own logo- please see uploaded. I have other file formats if you need (not sure one needed?)

Details for Business Card:
Fiona Kettlewood
Clinical Psychologist BPsych, BPsych (Hons), MPsych (Clin), MAPS
T: 0457260714 | F: 08 71526804
E: hello@harbourlightmindcarestudio.com.au
W: harbourlightmindcarestudio.com.au

Industry/Entity Type

Health

Contact Information for Business Card

Logo plus details above (couldn't write in this section)

```html
<!DOCTYPE html>
<html lang="en">
<head>
<meta charset="utf-8">
<title>Harbourlight Mindcare Studio – Business Cards</title>
<link rel="stylesheet" href="https://fonts.googleapis.com/css2?family=Cinzel:wght@500&family=Montserrat:wght@400;500&display=swap">
<style>
  :root {
    --stage: #1c1c1c;
    --card: #232323;
    --pattern-light: #2c2c2c;
    --pattern-dark: #141414;
    --brand-blue: #1f6aa8;
    --accent-blue: #2a8fc9;
    --ink-light: #e6e6e6;
    --rule: #cfcfcf;
    --white: #ffffff;
  }
  * { margin: 0; padding: 0; box-sizing: border-box; }
  html, body {
    width: 1200px; height: 874px; overflow: hidden;
    background: var(--stage);
    font-family: "Montserrat", Arial, sans-serif;
  }
  .canvas { position: relative; width: 1200px; height: 874px; }
  .card {
    position: absolute; left: 300px; width: 600px; height: 343px;
    border-radius: 3px; overflow: hidden;
  }
  .card--front { top: 52px; }
  .card--back { top: 447px; background: var(--card); }

  .pattern-fill {
    position: absolute; inset: 0;
    background: linear-gradient(135deg, var(--pattern-light) 0%, #1f1f1f 55%, var(--pattern-dark) 100%);
  }
  .brand-mark {
    position: absolute; display: flex; align-items: center; gap: 10px;
    font-family: "Cinzel", Georgia, serif; font-weight: 500;
  }
  .brand-mark__dot { width: 14px; height: 14px; border-radius: 50%; flex: none; }
  .card--front .brand-mark { right: 34px; bottom: 40px; color: var(--white); font-size: 15px; letter-spacing: 1px; }
  .card--front .brand-mark__dot { background: var(--white); }

  .card--back .brand-mark {
    right: 36px; top: 118px; color: var(--brand-blue);
    font-size: 18px; letter-spacing: 1px; flex-direction: column; gap: 10px; text-align: center;
  }
  .card--back .brand-mark__dot { width: 22px; height: 22px; background: var(--brand-blue); }

  .holder { position: absolute; left: 40px; top: 126px; }
  .holder__name {
    font-family: "Cinzel", Georgia, serif; font-weight: 500;
    font-size: 24px; letter-spacing: 1.5px; color: var(--brand-blue); text-transform: uppercase;
  }
  .holder__title { font-size: 13px; color: var(--accent-blue); margin-top: 2px; }
  .holder__quals { font-size: 8.5px; color: var(--accent-blue); margin-top: 2px; }
  .divider {
    position: absolute; left: 40px; right: 40px; top: 204px;
    height: 1px; background: var(--rule);
  }
  .contacts { position: absolute; left: 40px; top: 218px; list-style: none; color: var(--ink-light); font-size: 12px; }
  .contacts li { display: flex; align-items: center; gap: 8px; height: 20px; }
  .contacts svg { width: 11px; height: 11px; fill: var(--accent-blue); flex: none; }
  .contacts .sep { display: inline-flex; align-items: center; gap: 6px; margin-left: 8px; }
</style>
</head>
<body>
<main class="canvas">

  <section class="card card--front">
    <div class="pattern-fill" role="img" aria-label="Embossed tone-on-tone floral pattern in black"></div>
    <div class="brand-mark">
      <span class="brand-mark__dot"></span>
      <span class="brand-mark__name">Harbourlight Mindcare Studio</span>
    </div>
  </section>

  <section class="card card--back">
    <div class="holder">
      <h1 class="holder__name">Fiona Kettlewood</h1>
      <p class="holder__title">Clinical Psychologist BPsych,</p>
      <p class="holder__quals">BPsych (Hons), MPsych (Clin), MAPS</p>
    </div>

    <div class="divider"></div>

    <ul class="contacts">
      <li>
        <svg viewBox="0 0 24 24"><path d="M6.6 10.8a15 15 0 0 0 6.6 6.6l2.2-2.2c.3-.3.7-.4 1-.2 1.1.4 2.3.6 3.6.6.6 0 1 .4 1 1V20c0 .6-.4 1-1 1A17 17 0 0 1 3 4c0-.6.4-1 1-1h3.5c.6 0 1 .4 1 1 0 1.3.2 2.5.6 3.6.1.3 0 .7-.2 1z"/></svg>
        <span>0457260714</span>
        <span class="sep">
          <svg viewBox="0 0 24 24"><path d="M6 3h10v5H6zM3 9h18v9h-3v3H6v-3H3zm5 7v3h8v-3z"/></svg>
          <span>08 71526804</span>
        </span>
      </li>
      <li>
        <svg viewBox="0 0 24 24"><path d="M2 5h20v14H2zm2 2v.5l8 5 8-5V7l-8 5z"/></svg>
        <span>hello@harbourlightmindcarestudio.com.au</span>
      </li>
      <li>
        <svg viewBox="0 0 24 24"><circle cx="12" cy="12" r="10"/></svg>
        <span>harbourlightmindcarestudio.com.au</span>
      </li>
    </ul>

    <div class="brand-mark">
      <span class="brand-mark__dot"></span>
      <span class="brand-mark__name">Harbourlight<br>Mindcare Studio</span>
    </div>
  </section>

</main>
</body>
</html>
```